Infografiken für Unternehmensberater
Zielgruppe
Unternehmensberater Zielgruppe Management Beratung ganzheitlich. Wie können Managerinnen noch erfolgreicher sein - durch und mit ihre Werte leben.
Aufgabenstellung
Ich habe den Prozess KORVELT ® registriert und möchte hierzu ein stimmiges Design das ich online verwenden kann und auch in meinen Präsentationen sowie als Kapitel Überschriften in meinem Buch zu dem Thema als auch auf meiner Homepage.
KORVELT® nach Halbig ist mein Management Prozess für erfolgreiche Managerinnen. Aus meiner 30jährigen Führungserfahrung.
DI - Dialog Aktives Zuhören, Dialogue Active Listening
N - Nenne und Erkenne das Problem: Name and Recognize the Problem
A - Anerkennung und Wertschätzung: Acknowledgement and Appreciation
M - Meine Stärken kennen und diese einsetzen je nach Situation: Know My Strengths and Apply Them According to the Situation
I - Intensives Handeln ins Tun kommen – machen: Intense Action into Doing – Execute
S - den Sinn kennen das warum als Grundlage des Prozesses: See and Knowing the Purpose, the Why as the Basis of the Process
Es muss nicht unbedingt in einem Kreis dargestellt werden - hier bin ich offen für gute Ideen.
Designelement können von der Homepage übernommen werden.

```html
<!DOCTYPE html>
<html lang="de">
<head>
<meta charset="utf-8">
<title>Der KORVELT Prozess nach Halbig</title>
<link rel="stylesheet" href="https://fonts.googleapis.com/css2?family=Montserrat:wght@500;600;700&family=Oswald:wght@400;500&display=swap">
<style>
  :root {
    --stage: #8d8f90;
    --sky-light: #c9eafc;
    --sky-mid: #9fd8f3;
    --sky-deep: #72c3ea;
    --corner-shade: #5f9fc8;
    --navy: #1f3566;
    --ink-blue: #2b5a86;
    --white: #ffffff;
    --footer-grey: #e6e7e9;
    --wordmark: #3b3c3e;
    --caption-grey: #5a5b5d;
    --icon-fill: #6cc4ec;
    --title-cyan: #1aa4e6;
  }
  * { margin: 0; padding: 0; box-sizing: border-box; }
  html, body {
    width: 1166px;
    height: 1200px;
    overflow: hidden;
    background: var(--stage);
  }
  .infographic {
    position: absolute;
    left: 0;
    top: 106px;
    width: 1166px;
    height: 988px;
    display: block;
  }
  .step-title { font-family: "Montserrat", sans-serif; font-weight: 700; font-size: 44px; fill: var(--white); }
  .step-initial { font-family: "Montserrat", sans-serif; font-weight: 700; font-size: 40px; fill: var(--ink-blue); }
  .note-light { font-family: "Montserrat", sans-serif; font-weight: 500; font-size: 30px; fill: var(--white); }
  .note-dark { font-family: "Montserrat", sans-serif; font-weight: 500; font-size: 30px; fill: var(--ink-blue); }
  .leader { stroke: var(--white); stroke-width: 2; }
  .leader-dot { fill: var(--white); }
  .process-title { font-family: "Oswald", sans-serif; font-weight: 500; font-size: 74px; }
  .process-title .t-der, .process-title .t-rest { fill: var(--title-cyan); }
  .process-title .t-name { fill: var(--white); letter-spacing: 14px; }
  .icon-slot { fill: var(--icon-fill); opacity: 0.55; }
  .brand-name { font-family: "Montserrat", sans-serif; font-weight: 500; font-size: 56px; fill: var(--wordmark); }
  .brand-tagline { font-family: "Montserrat", sans-serif; font-weight: 500; font-size: 15px; letter-spacing: 2.5px; fill: var(--caption-grey); }
</style>
</head>
<body>
<svg class="infographic" viewBox="0 0 1733 1468" xmlns="http://www.w3.org/2000/svg">
  <defs>
    <linearGradient id="sky" x1="0" y1="0" x2="1" y2="1">
      <stop offset="0" stop-color="var(--sky-light)"/>
      <stop offset="0.5" stop-color="var(--sky-mid)"/>
      <stop offset="0.9" stop-color="var(--sky-deep)"/>
      <stop offset="1" stop-color="var(--corner-shade)"/>
    </linearGradient>
    <linearGradient id="loop-back" gradientUnits="userSpaceOnUse" x1="200" y1="0" x2="1600" y2="0">
      <stop offset="0" stop-color="#5a9ccc"/>
      <stop offset="0.3" stop-color="#3d5d97"/>
      <stop offset="0.5" stop-color="#2a2a68"/>
      <stop offset="0.75" stop-color="#1e4f96"/>
      <stop offset="1" stop-color="#0a8fd6"/>
    </linearGradient>
    <linearGradient id="loop-front" gradientUnits="userSpaceOnUse" x1="200" y1="0" x2="1350" y2="0">
      <stop offset="0" stop-color="#4f8fc2"/>
      <stop offset="0.35" stop-color="#1f3e73"/>
      <stop offset="0.6" stop-color="#1a5f92"/>
      <stop offset="1" stop-color="#1d3a6b"/>
    </linearGradient>
  </defs>

  <!-- Card background -->
  <rect class="card" x="0" y="0" width="1733" height="1468" fill="url(#sky)"/>

  <!-- Infinity band -->
  <g class="infinity">
    <path d="M675.4 533.4 L1052.6 910.6 A265 265 0 1 0 1052.6 533.4" fill="none" stroke="url(#loop-back)" stroke-width="220"/>
    <path d="M1052.6 533.4 L675.4 910.6 A265 265 0 1 1 675.4 533.4" fill="none" stroke="url(#loop-front)" stroke-width="220"/>
    <text class="process-title" transform="translate(864 722) rotate(-45)" text-anchor="middle" y="26">
      <tspan class="t-der">Der </tspan><tspan class="t-name">KORVELT</tspan><tspan class="t-rest"> Prozess nach Halbig</tspan>
    </text>
  </g>

  <!-- Icon areas -->
  <rect class="icon-slot" x="130" y="252" width="190" height="178" rx="14" role="img" aria-label="Icon: Person steigt eine Treppe hinauf"/>
  <rect class="icon-slot" x="553" y="84" width="168" height="162" rx="14" role="img" aria-label="Icon: zwei Personen beim Händedruck"/>
  <rect class="icon-slot" x="1204" y="136" width="188" height="200" rx="14" role="img" aria-label="Icon: Lupe mit Herz und Person"/>
  <rect class="icon-slot" x="1164" y="640" width="182" height="178" rx="14" role="img" aria-label="Icon: zwei Personen mit Austauschpfeilen"/>
  <rect class="icon-slot" x="748" y="1026" width="178" height="156" rx="14" role="img" aria-label="Icon: Person mit Pfeilen in alle Richtungen"/>
  <rect class="icon-slot" x="170" y="948" width="180" height="148" rx="14" role="img" aria-label="Icon: zwei Personen mit Sprechblase"/>

  <!-- N: Nennen -->
  <g class="step step-nennen">
    <line class="leader" x1="186" y1="475" x2="186" y2="592"/>
    <circle class="leader-dot" cx="186" cy="475" r="5"/>
    <text class="note-light" x="203" y="489">WO DRÜCKT</text>
    <text class="note-light" x="203" y="526">DER SCHUH</text>
    <circle cx="188" cy="614" r="23" fill="var(--white)"/>
    <text class="step-initial" x="188" y="629" text-anchor="middle">N</text>
    <text class="step-title" x="212" y="630">ENNEN</text>
  </g>

  <!-- A: Anerkennung -->
  <g class="step step-anerkennung">
    <line class="leader" x1="525" y1="282" x2="525" y2="408"/>
    <circle class="leader-dot" cx="525" cy="282" r="5"/>
    <text class="note-dark" x="548" y="297">WERTSCHÄTZUNG.</text>
    <text class="note-dark" x="548" y="345">RESPEKT.</text>
    <circle cx="525" cy="430" r="23" fill="var(--white)"/>
    <text class="step-initial" x="525" y="445" text-anchor="middle">A</text>
    <text class="step-title" x="549" y="445">NERKENNUNG</text>
  </g>

  <!-- S: Die Sinnfrage -->
  <g class="step step-sinnfrage">
    <line class="leader" x1="1407" y1="218" x2="1407" y2="374"/>
    <circle class="leader-dot" cx="1407" cy="218" r="5"/>
    <text class="note-dark" x="1428" y="232">WARUM</text>
    <text class="note-dark" x="1428" y="269">MACHEN</text>
    <text class="note-dark" x="1428" y="306">WIR ES?</text>
    <text class="step-title" x="1300" y="412">DIE</text>
    <circle cx="1406" cy="396" r="23" fill="var(--white)"/>
    <text class="step-initial" x="1406" y="411" text-anchor="middle">S</text>
    <text class="step-title" x="1430" y="412">INNFRAGE</text>
  </g>

  <!-- I: Intensives Handeln -->
  <g class="step step-handeln">
    <line class="leader" x1="1368" y1="630" x2="1368" y2="770"/>
    <circle class="leader-dot" cx="1368" cy="770" r="5"/>
    <circle cx="1368" cy="608" r="23" fill="var(--white)"/>
    <text class="step-initial" x="1368" y="623" text-anchor="middle">I</text>
    <text class="step-title" x="1390" y="624">NTENSIVES</text>
    <text class="step-title" x="1390" y="675">HANDELN</text>
    <text class="note-light" x="1390" y="735">VERANTWORTUNG</text>
    <text class="note-light" x="1390" y="772">ÜBERNEHMEN</text>
  </g>

  <!-- M: Meine Stärken kennen -->
  <g class="step step-staerken">
    <line class="leader" x1="952" y1="982" x2="952" y2="1122"/>
    <circle class="leader-dot" cx="952" cy="1122" r="5"/>
    <circle cx="952" cy="960" r="23" fill="var(--white)"/>
    <text class="step-initial" x="952" y="975" text-anchor="middle">M</text>
    <text class="step-title" x="976" y="976">EINE STÄRKEN KENNEN</text>
    <text class="note-dark" x="955" y="1173" text-anchor="middle">WAS</text>
    <text class="note-dark" x="955" y="1210" text-anchor="middle">KANN ICH</text>
    <text class="note-dark" x="955" y="1247" text-anchor="middle">BEITRAGEN</text>
  </g>

  <!-- DI: Dialog -->
  <g class="step step-dialog">
    <line class="leader" x1="130" y1="888" x2="130" y2="1213"/>
    <circle class="leader-dot" cx="130" cy="1213" r="5"/>
    <rect x="104" y="842" width="56" height="48" rx="24" fill="var(--white)"/>
    <text class="step-initial" x="132" y="881" text-anchor="middle">DI</text>
    <text class="step-title" x="160" y="882">ALOG</text>
    <text class="note-dark" x="152" y="1137">KOMMUNIZIEREN.</text>
    <text class="note-dark" x="152" y="1185">AKTIVES</text>
    <text class="note-dark" x="152" y="1222">ZUHÖREN.</text>
  </g>

  <!-- Footer -->
  <g class="footer">
    <rect x="0" y="1404" width="1733" height="64" fill="var(--footer-grey)"/>
    <polygon points="1035,1404 1178,1228 1733,1228 1733,1404" fill="var(--footer-grey)"/>
    <line x1="1302" y1="1268" x2="1302" y2="1416" stroke="#b9babc" stroke-width="2"/>
    <text class="brand-name" x="1690" y="1342" text-anchor="end">halbigjonas</text>
    <text class="brand-tagline" x="1690" y="1380" text-anchor="end">MENTAL &amp; BUSINESSCOACHING</text>
  </g>
</svg>
</body>
</html>
```